KAZ Freightworks #ALLKAZ Business Cards & Letterhead

I am looking to business cards designed for our organization. We are currently undergoing a small re-branding that is taking place. Our organization is called KAZ Freightworks and we are headquartered in Phoenix, AZ. We primarily provide transportation and logistics services to the Meridel Parcel Bureau who is our largest customer. I would like to see a design that incorporates name, title, contact info, website, and address (this will be different depending on the employee). I would also like to see some color on the business card using our logo colors or a variation. I would like our logo on the back of the business card with the website displayed. The final design should communicate that we are a next generation transportation operate that focuses on being driver-first, customer-centric, innovative, and sustainable.We would also like our #ALLKAZ catch phrase incorporated as well.
Updates

Decision maker traveling outside of the country until Monday, November 25th.

Target Market(s)

Transportation & Logistics

Industry/Entity Type

Trucking Company

Contact Information for Business Card

-First and Last Name
-Position Title
-Contact Phone
-Contact Email
-Physical Address

Font styles to use
Serif

Colors

Designer to choose colors to be used in the design.

Requirements
Must have
• -KAZ logo prominently displayed
• -#ALLKAZ catch phrase used
• -Some amount of color, design gradient, etc.
• -Logo on the back with website listed (https://www.kazfreightco.example)

```html
<!DOCTYPE html>
<html lang="en">
<head>
<meta charset="utf-8">
<title>KAZ Freightworks – Business Card</title>
<link rel="stylesheet" href="https://fonts.googleapis.com/css2?family=Lato:wght@400;700;900&display=swap">
<style>
  :root {
    --page-bg: #ecebe8;
    --card-white: #ffffff;
    --brand-green: #7bbf41;
    --brand-green-mid: #4f9a4a;
    --brand-teal: #0d3b47;
    --ink: #12323b;
    --white: #ffffff;
  }
  * { margin: 0; padding: 0; box-sizing: border-box; }
  html, body {
    width: 1000px; height: 1200px; overflow: hidden;
    background: var(--page-bg);
    font-family: "Lato", Arial, sans-serif;
  }
  .canvas { position: relative; width: 1000px; height: 1200px; }

  .card {
    position: absolute;
    border-radius: 20px;
    overflow: hidden;
    box-shadow: 0 6px 14px rgba(0,0,0,0.18);
  }
  .card-front { left: 112px; top: 131px; width: 777px; height: 446px; background: var(--card-white); }
  .card-back {
    left: 110px; top: 623px; width: 782px; height: 445px;
    background: linear-gradient(180deg, var(--brand-green) 0%, var(--brand-green-mid) 35%, #27604f 65%, var(--brand-teal) 100%);
  }

  .brand-ring {
    position: absolute;
    border-radius: 50%;
    display: flex; align-items: center; justify-content: center;
    font-weight: 900;
    letter-spacing: 1px;
  }
  .card-front .brand-ring {
    left: 91px; top: 100px; width: 222px; height: 222px;
    border: 7px solid var(--brand-green);
    color: var(--brand-teal);
    font-size: 78px;
  }
  .card-back .brand-ring {
    left: 274px; top: 97px; width: 234px; height: 234px;
    border: 6px solid var(--white);
    color: var(--white);
    font-size: 82px;
  }

  .divider {
    position: absolute; left: 350px; top: 105px;
    width: 2px; height: 216px; background: var(--brand-green);
  }
  .contact { position: absolute; left: 393px; top: 98px; color: var(--ink); }
  .contact-name {
    color: var(--brand-green); font-weight: 700; font-size: 23px;
    text-transform: uppercase; letter-spacing: 0.3px; line-height: 28px;
  }
  .contact-title { font-size: 18px; line-height: 24px; }
  .contact-address { margin-top: 12px; font-size: 18px; line-height: 25px; }
  .contact-list { list-style: none; margin-top: 11px; }
  .contact-list li { display: flex; align-items: center; font-size: 18px; line-height: 25px; }
  .contact-list svg { width: 15px; height: 15px; margin-right: 10px; fill: var(--brand-green); flex: none; }

  .band { position: absolute; left: 0; bottom: 0; width: 100%; height: 100%; }
  .band-text {
    position: absolute; left: 0; width: 100%; text-align: center;
    color: var(--white); font-size: 22px; font-weight: 700;
  }
  .card-front .band-text { top: 402px; letter-spacing: 3px; }
  .card-back .band-text { top: 400px; letter-spacing: 2px; font-size: 21px; }
</style>
</head>
<body>
<div class="canvas">

  <section class="card card-front" aria-label="Business card front">
    <div class="brand-ring">KAZ</div>
    <div class="divider"></div>
    <div class="contact">
      <p class="contact-name">Dana Whitlock</p>
      <p class="contact-title">Owner</p>
      <p class="contact-address">1180 Larkspur Avenue, Fennmore<br>AZ 8, United States</p>
      <ul class="contact-list">
        <li><svg viewBox="0 0 24 24"><path d="M6.6 10.8a15.1 15.1 0 0 0 6.6 6.6l2.2-2.2c.3-.3.7-.4 1-.2 1.1.4 2.3.6 3.6.6.6 0 1 .4 1 1V20c0 .6-.4 1-1 1A17 17 0 0 1 3 4c0-.6.4-1 1-1h3.5c.6 0 1 .4 1 1 0 1.3.2 2.5.6 3.6.1.3 0 .7-.2 1z"/></svg>000-000-000-000</li>
        <li><svg viewBox="0 0 24 24"><path d="M6 2h12v5H6zM4 8h16a2 2 0 0 1 2 2v7h-4v5H6v-5H2v-7a2 2 0 0 1 2-2zm4 7v5h8v-5z"/></svg>000-000-000-000</li>
        <li><svg viewBox="0 0 24 24"><path d="M2 5h20v14H2zm2 2v.5l8 5.5 8-5.5V7zm0 3v7h16v-7l-8 5.5z"/></svg>info@kazfreightco.example</li>
        <li><svg viewBox="0 0 24 24"><path d="M12 2a10 10 0 1 0 0 20 10 10 0 0 0 0-20zm6.9 6h-3a15 15 0 0 0-1.3-3.9A8 8 0 0 1 18.9 8zM12 4c.8 1.1 1.5 2.5 1.9 4h-3.8c.4-1.5 1.1-2.9 1.9-4zM4.3 14a8 8 0 0 1 0-4h3.4a16 16 0 0 0 0 4zm.8 2h3a15 15 0 0 0 1.3 3.9A8 8 0 0 1 5.1 16zm3-8h-3a8 8 0 0 1 4.3-3.9A15 15 0 0 0 8.1 8zM12 20c-.8-1.1-1.5-2.5-1.9-4h3.8c-.4 1.5-1.1 2.9-1.9 4zm2.3-6H9.7a14 14 0 0 1 0-4h4.6a14 14 0 0 1 0 4zm.3 5.9a15 15 0 0 0 1.3-3.9h3a8 8 0 0 1-4.3 3.9zM16.3 14a16 16 0 0 0 0-4h3.4a8 8 0 0 1 0 4z"/></svg>www.kazfreightco.example</li>
      </ul>
    </div>
    <svg class="band" viewBox="0 0 777 446" preserveAspectRatio="none" aria-hidden="true">
      <defs>
        <linearGradient id="front-band" x1="0" y1="0" x2="0" y2="1">
          <stop offset="0" stop-color="#7bbf41"/>
          <stop offset="0.55" stop-color="#4e9a48"/>
          <stop offset="1" stop-color="#1f5a4d"/>
        </linearGradient>
      </defs>
      <path d="M0 446 L0 440 Q388 318 777 440 L777 446 Z" fill="url(#front-band)"/>
    </svg>
    <p class="band-text">#ALLKAZ</p>
  </section>

  <section class="card card-back" aria-label="Business card back">
    <div class="brand-ring">KAZ</div>
    <svg class="band" viewBox="0 0 782 445" preserveAspectRatio="none" aria-hidden="true">
      <defs>
        <linearGradient id="back-band" x1="0" y1="0" x2="0" y2="1">
          <stop offset="0" stop-color="#7bbf41"/>
          <stop offset="0.12" stop-color="#3f8a4c"/>
          <stop offset="0.5" stop-color="#1d5550"/>
          <stop offset="1" stop-color="#0d3b47"/>
        </linearGradient>
      </defs>
      <path d="M0 445 L0 436 Q391 318 782 436 L782 445 Z" fill="url(#back-band)"/>
    </svg>
    <p class="band-text">www.kazfreightco.example</p>
  </section>

</div>
</body>
</html>
```